Corvello Business card

I got my logo so I need to have that on my business card!!

Thanks
Updates

Reason: Hi designers, i will be deciding my logo by this weekend!!! As soon as I decide i will post my logo for your application Thanks Teodoro

I Just sent my logo for your attention!!!

Target Market(s)

My costumers will be enginners from shipyard industry!

Industry/Entity Type

Business

Requirements
Must have
• My future logo

```html
<!DOCTYPE html>
<html lang="en">
<head>
<meta charset="UTF-8">
<title>Corvello Business Card</title>
<link href="https://fonts.googleapis.com/css2?family=PT+Sans:wght@400;700&display=swap" rel="stylesheet">
<style>
  :root {
    --backdrop: #1f1f1f;
    --card-white: #ffffff;
    --brand-blue: #00adef;
    --deep-blue: #0b3f7a;
    --mid-blue: #1c6fb8;
    --sun-yellow: #ffd200;
    --amber: #f7a800;
    --soft-grey: #ececec;
    --ink-dark: #1b1b1b;
    --ink-grey: #5a5a5a;
    --ink-light: #7a7a7a;
  }
  * { box-sizing: border-box; margin: 0; padding: 0; }
  html, body {
    width: 1140px; height: 1200px; overflow: hidden;
    background: var(--backdrop);
    font-family: "PT Sans", Arial, sans-serif;
  }
  .sheet {
    width: 1140px; height: 1200px;
    display: flex; flex-direction: column; align-items: center; justify-content: space-evenly;
  }
  .card {
    position: relative; width: 900px; height: 553px; overflow: hidden;
    box-shadow: 0 10px 30px rgba(0,0,0,.45);
  }
  .card-front { background: var(--card-white); }
  .card-back { background: var(--brand-blue); }

  .top-band {
    position: absolute; left: 0; top: 0; width: 100%; height: 150px;
    background: linear-gradient(90deg, var(--deep-blue) 0%, var(--mid-blue) 22%, var(--amber) 45%, var(--sun-yellow) 100%);
  }
  .side-tone {
    position: absolute; left: 380px; top: 150px; width: 520px; height: 403px;
    background: linear-gradient(90deg, var(--card-white) 0%, var(--soft-grey) 55%, var(--card-white) 100%);
  }

  .front-brand {
    position: absolute; left: 80px; top: 296px;
    font-weight: 700; font-size: 64px; letter-spacing: 0.5px;
    color: var(--ink-dark); line-height: 1;
  }
  .contact { position: absolute; left: 560px; top: 282px; color: var(--ink-grey); }
  .contact-name { font-size: 36px; font-weight: 700; color: var(--ink-grey); line-height: 1; }
  .contact-role { font-size: 22px; color: var(--ink-light); margin-top: 4px; line-height: 1.1; }
  .contact-list { list-style: none; margin-top: 14px; }
  .contact-list li {
    display: flex; align-items: center; gap: 10px;
    font-size: 24px; line-height: 1; height: 33px; color: var(--ink-grey);
  }
  .contact-icon {
    width: 26px; height: 28px; background: var(--mid-blue);
    display: flex; align-items: center; justify-content: center; flex: none;
  }
  .contact-icon svg { width: 18px; height: 18px; }

  .back-brand {
    position: absolute; left: 0; right: 0; top: 302px; text-align: center;
    font-weight: 700; font-size: 96px; color: var(--card-white); line-height: 1;
  }
  .back-mark {
    position: absolute; left: 408px; top: 160px; width: 84px; height: 84px;
    border-radius: 50%; background: var(--card-white);
  }
</style>
</head>
<body>
<main class="sheet">

  <section class="card card-front" aria-label="Business card front">
    <div class="top-band" role="img" aria-label="Blue and yellow wave decoration across the top"></div>
    <div class="side-tone" role="img" aria-label="Soft grey ring decoration behind the contact details"></div>

    <div class="front-brand">CORVELLO</div>

    <div class="contact">
      <p class="contact-name">Teodoro Marin</p>
      <p class="contact-role">Manager/Director</p>
      <ul class="contact-list">
        <li><span class="contact-icon"><svg viewBox="0 0 24 24"><path fill="#fff" d="M12 2a7 7 0 0 0-7 7c0 5 7 13 7 13s7-8 7-13a7 7 0 0 0-7-7zm0 9.5A2.5 2.5 0 1 1 12 6.5a2.5 2.5 0 0 1 0 5z"/></svg></span>48 Harbour Quay</li>
        <li><span class="contact-icon"><svg viewBox="0 0 24 24"><path fill="#fff" d="M3 5h18v14H3zm2 2v.5l7 5 7-5V7z"/></svg></span>name@corvello.com</li>
        <li><span class="contact-icon"><svg viewBox="0 0 24 24"><path fill="#fff" d="M3 5h18v14H3zm2 2v.5l7 5 7-5V7z"/></svg></span>name@corvello.com</li>
        <li><span class="contact-icon"><svg viewBox="0 0 24 24"><circle cx="12" cy="12" r="9" fill="none" stroke="#fff" stroke-width="2"/><path d="M3 12h18M12 3c3 3 3 15 0 18M12 3c-3 3-3 15 0 18" fill="none" stroke="#fff" stroke-width="1.6"/></svg></span>www.corvello.com</li>
      </ul>
    </div>
  </section>

  <section class="card card-back" aria-label="Business card back">
    <span class="back-mark"></span>
    <div class="back-brand">CORVELLO</div>
  </section>

</main>
</body>
</html>
```